Childcare Centre trifold brochure

Design a contemporary trifold brochure for a childcare centre that meets Australian printing requirements with supplied content, logo's, fonts and photo's. Please refer to the attached DL flyer front and back for similar possible style and content.

Target Market(s)

Families

Industry/Entity Type

Childcare

Requirements
Must have
• refer attached content, photo's, logo's and examples. Colours should be same as Pantone purple and green and or variations of. Refer attached dl flyer example.

```html
<!DOCTYPE html>
<html lang="en">
<head>
<meta charset="utf-8">
<title>Tiny Sprouts – Trifold Brochure</title>
<link href="https://fonts.googleapis.com/css2?family=Fredoka:wght@500;600;700&family=Open+Sans:ital,wght@0,400;0,600;0,700;1,700&display=swap" rel="stylesheet">
<style>
  :root{
    --purple:#a112ad;
    --purple-dark:#7d0b87;
    --green:#1fc21a;
    --green-dark:#16a012;
    --white:#ffffff;
    --ink:#333333;
    --page:#e9e9e9;
  }
  *{box-sizing:border-box;margin:0;padding:0}
  html,body{width:920px;height:1200px;overflow:hidden}
  body{background:var(--page);font-family:"Open Sans",Arial,sans-serif;color:var(--ink);position:relative}
  .sheet{position:absolute;left:40px;width:840px;height:590px;background:var(--white);overflow:hidden;box-shadow:0 2px 8px rgba(0,0,0,.18)}
  .sheet--outside{top:6px}
  .sheet--inside{top:604px}
  .sheet svg.backdrop{position:absolute;left:0;top:0}
  .abs{position:absolute}

  /* brand lockup */
  .brand{position:absolute;text-align:center;font-family:"Fredoka",sans-serif}
  .brand__dot{display:block;margin:0 auto 4px;border-radius:50%;background:var(--purple)}
  .brand__name{display:block;font-weight:700;line-height:1}
  .brand__tag{display:block;font-family:"Open Sans",sans-serif;font-weight:600;color:var(--green-dark);margin-top:3px}

  /* outside: left panel */
  .intro{left:31px;top:26px;width:226px;color:var(--white);font-size:11.3px;line-height:1.28;font-weight:600}
  .intro p{margin-bottom:13px}
  .award{position:absolute;left:0;width:240px;height:37px;background:var(--purple);color:var(--white);font-size:11px;font-weight:600;line-height:1.28;padding:2px 0 0 31px;border:2px solid var(--white);border-left:none}
  .quality-badge{left:60px;top:488px;width:160px;height:70px}

  /* outside: middle panel */
  .contact{left:279px;top:100px;width:296px;text-align:center;font-family:"Fredoka",sans-serif;font-weight:600;color:var(--purple);font-size:11.5px;line-height:1.6}
  .contact svg{vertical-align:-2px;margin-right:4px}
  .pill{position:absolute;left:334px;top:162px;width:184px;height:22px;border-radius:11px;background:var(--green);color:var(--white);font-family:"Fredoka",sans-serif;font-weight:700;font-size:11px;text-align:center;line-height:22px}
  .social{left:300px;top:194px;width:260px;display:flex;justify-content:center;gap:16px;font-family:"Fredoka",sans-serif;font-weight:600;font-size:9.5px;color:var(--purple)}
  .social span{display:flex;align-items:center;gap:4px}
  .social i{display:inline-block;width:13px;height:13px;border-radius:50%;background:#1a8fe3}
  .partner{border-radius:4px}
  .hours{left:297px;top:508px;color:var(--white);width:150px}
  .hours h3{font-family:"Fredoka",sans-serif;font-weight:700;font-size:17px;line-height:1.1}
  .hours p{font-size:12px;font-weight:600;line-height:1.3}
  .hours small{display:block;font-size:8.5px;font-weight:600}
  .enrol{left:454px;top:484px;width:80px;height:80px;border-radius:50%;background:var(--green);border:3px solid var(--white);color:var(--white);font-family:"Fredoka",sans-serif;font-weight:700;font-size:15px;line-height:1;display:flex;flex-direction:column;align-items:center;justify-content:center;transform:rotate(-6deg)}

  /* outside: right panel */
  .tagline{left:590px;top:480px;width:230px;text-align:center;font-family:"Fredoka",sans-serif;font-weight:500;color:var(--white);font-size:20px;line-height:1.4;letter-spacing:.5px}
  .webbar{left:559px;top:549px;width:281px;height:33px;background:var(--green);color:var(--white);font-family:"Fredoka",sans-serif;font-weight:700;font-size:15px;text-align:center;line-height:33px}

  /* inside */
  .col{font-size:8.3px;line-height:1.28;color:#3a3a3a}
  .col p{margin-bottom:10px}
  .col--left{left:33px;top:146px;width:212px}
  .col--mid{left:305px;top:186px;width:228px}
  .col--right{left:588px;top:218px;width:228px}
  .quote{left:444px;top:26px;width:366px;text-align:center;color:var(--white);font-size:12.8px;line-height:1.33}
  .quote strong{font-weight:700}
  .quote cite{display:block;margin-top:8px;font-size:11px;font-weight:700;font-style:italic;text-align:right;padding-right:98px}
  .closing{left:330px;top:536px;width:462px;text-align:center;color:var(--white);font-size:11.3px;line-height:1.38}
  .webcorner{left:30px;top:557px;color:var(--white);font-family:"Fredoka",sans-serif;font-weight:700;font-size:14px}
</style>
</head>
<body>

<!-- OUTSIDE -->
<section class="sheet sheet--outside">
  <svg class="backdrop" width="840" height="590" viewBox="0 0 840 590">
    <defs>
      <linearGradient id="paint" x1="0" y1="0" x2="1" y2="1">
        <stop offset="0" stop-color="#f4d9c6"/><stop offset=".5" stop-color="#f0c64a"/><stop offset="1" stop-color="#3a8ad6"/>
      </linearGradient>
      <linearGradient id="garden" x1="0" y1="0" x2="1" y2="1">
        <stop offset="0" stop-color="#7a6a55"/><stop offset=".45" stop-color="#8b4fb5"/><stop offset="1" stop-color="#b08a5a"/>
      </linearGradient>
      <linearGradient id="kitchen" x1="0" y1="0" x2="1" y2="1">
        <stop offset="0" stop-color="#8a7458"/><stop offset=".4" stop-color="#6e45b0"/><stop offset=".75" stop-color="#c94a3c"/><stop offset="1" stop-color="#e8c83a"/>
      </linearGradient>
    </defs>
    <rect x="0" y="0" width="279" height="462" fill="var(--green)"/>
    <path d="M279,300 C305,430 400,478 520,472 C610,466 660,420 840,240 L840,590 L279,590 Z" fill="var(--purple)"/>
    <path d="M279,300 C305,430 400,478 520,472" fill="none" stroke="var(--green)" stroke-width="5"/>
    <g role="img" aria-label="Photo of a child holding up paint-covered hands">
      <circle cx="345" cy="318" r="64" fill="url(#paint)"/>
    </g>
    <g role="img" aria-label="Photo of children chopping vegetables outdoors on a garden table">
      <circle cx="706" cy="304" r="133" fill="url(#kitchen)" stroke="var(--purple)" stroke-width="6"/>
    </g>
    <g role="img" aria-label="Photo of a child in a purple hat working with tools in the garden">
      <circle cx="501" cy="404" r="92" fill="url(#garden)" stroke="var(--green)" stroke-width="6"/>
    </g>
    <g fill="none" stroke="var(--white)" stroke-width="2.2" stroke-linecap="round">
      <circle cx="339" cy="460" r="26"/>
      <path d="M339,444 V460 L350,468"/>
      <path d="M316,438 A10,10 0 0 1 330,431"/>
      <path d="M362,438 A10,10 0 0 0 348,431"/>
      <path d="M322,484 L316,491 M356,484 L362,491"/>
    </g>
  </svg>

  <div class="abs intro">
    <p>We are a Reggio Emilia inspired Childcare Centre offering long day care and a Nature Kindergarten program for 3 – 6-year olds.</p>
    <p>At the core of our program is a Child-First ‘emergent curriculum’. An emergent Curriculum can be defined as a way of supporting learning that is based on the children’s interests.</p>
    <p>Learning occurs naturally, children thrive and learn best when their interests are considered and captured.</p>
    <p>Which means our Educators act as mentors for the children as they guide them through the adventure of learning outdoors in academic subjects such as science, technology, engineering</p>
  </div>
  <div class="award" style="top:330px">Finalist, Regional Early Learning Service Award, 2018, 2017 &amp; 2016</div>
  <div class="award" style="top:370px">State winner, Centre Leadership Award 2018</div>
  <div class="award" style="top:410px">Finalist, Centre Leadership Award, 2016 and maths (STEM).</div>
  <div class="abs quality-badge" role="img" aria-label="Quality rating certificate badge">
    <svg width="160" height="70"><rect x="0" y="14" width="110" height="42" rx="4" fill="#f3a63b" opacity=".85"/><polygon points="112,6 158,20 146,64 116,52" fill="#9a3fb8" opacity=".85"/></svg>
  </div>

  <div class="brand" style="left:279px;top:18px;width:296px">
    <span class="brand__dot" style="width:26px;height:26px"></span>
    <span class="brand__name" style="font-size:15px;color:var(--purple)">Tiny Sprouts</span>
    <span class="brand__tag" style="font-size:5.5px">Early Development &amp; Education Centre</span>
  </div>
  <div class="abs contact">
    <div><svg width="9" height="11" viewBox="0 0 9 11"><path d="M4.5,0 A4.5,4.5 0 0 1 9,4.5 C9,7 4.5,11 4.5,11 C4.5,11 0,7 0,4.5 A4.5,4.5 0 0 1 4.5,0Z" fill="var(--green)"/><circle cx="4.5" cy="4.3" r="1.6" fill="#fff"/></svg>18 Banksia Road, Greenvale</div>
    <div><svg width="11" height="10" viewBox="0 0 11 10"><path d="M0,5 L11,0 L7,10 L5,6 Z" fill="var(--green)"/></svg>hello@tinysprouts.example</div>
    <div><svg width="10" height="10" viewBox="0 0 10 10"><path d="M2,0 L4,3 L3,4 C3.6,5.6 4.4,6.4 6,7 L7,6 L10,8 L9,10 C4,10 0,6 0,1 Z" fill="var(--green)"/></svg>08 9000 1234</div>
  </div>
  <div class="pill">www.tinysprouts.example</div>
  <div class="abs social">
    <span><i></i>tinysproutsKids</span>
    <span><i></i>@TinySproutsKids</span>
  </div>
  <div class="abs partner" role="img" aria-label="Partner award badge" style="left:468px;top:236px;width:34px;height:38px;background:#f2b21a;opacity:.8"></div>
  <div class="abs partner" role="img" aria-label="Partner listing badge" style="left:512px;top:244px;width:22px;height:30px;background:#1aa7d8"></div>

  <div class="abs hours">
    <h3>Opening Hours</h3>
    <p>6:00am to 6:00pm<br>Monday to Friday<small>(except public holidays)</small></p>
  </div>
  <div class="abs enrol"><span>ENROL</span><span>NOW</span></div>

  <div class="brand" style="left:580px;top:16px;width:242px">
    <span class="brand__dot" style="width:40px;height:40px"></span>
    <span class="brand__name" style="font-size:22px;color:var(--purple)">Tiny Sprouts</span>
    <span class="brand__tag" style="font-size:7.5px">Early Development &amp; Education Centre</span>
  </div>
  <div class="abs tagline">Tiny seeds today,<br>tall trees tomorrow</div>
  <div class="abs webbar">www.tinysprouts.example</div>
</section>

<!-- INSIDE -->
<section class="sheet sheet--inside">
  <svg class="backdrop" width="840" height="590" viewBox="0 0 840 590">
    <defs>
      <linearGradient id="yard" x1="0" y1="0" x2="0" y2="1">
        <stop offset="0" stop-color="#ffffff"/><stop offset=".45" stop-color="#f1efea"/><stop offset="1" stop-color="#d9d1c4"/>
      </linearGradient>
      <linearGradient id="creek" x1="0" y1="0" x2="1" y2="1">
        <stop offset="0" stop-color="#8b7a62"/><stop offset=".5" stop-color="#b04fb0"/><stop offset="1" stop-color="#6f5c46"/>
      </linearGradient>
      <linearGradient id="dig" x1="0" y1="0" x2="1" y2="1">
        <stop offset="0" stop-color="#8a4fc0"/><stop offset=".5" stop-color="#d8d4cf"/><stop offset="1" stop-color="#9a7a55"/>
      </linearGradient>
    </defs>
    <rect role="img" aria-label="Faint photo of the nature playground used as a backdrop" x="0" y="0" width="840" height="590" fill="url(#yard)"/>
    <path d="M300,0 H840 V146 H420 A84,84 0 0 1 300,0 Z" fill="var(--green)"/>
    <path d="M420,149 H836 L830,154 H420 Z" fill="var(--purple)"/>
    <g role="img" aria-label="Photo of children in purple hats crossing a creek bed on logs">
      <circle cx="349" cy="60" r="64" fill="url(#creek)" stroke="var(--green)" stroke-width="5"/>
    </g>
    <g role="img" aria-label="Photo of a child using a hand tool on a log">
      <circle cx="777" cy="157" r="45" fill="url(#creek)" stroke="var(--green)" stroke-width="5"/>
    </g>
    <rect x="272" y="529" width="568" height="61" fill="var(--green)"/>
    <path d="M0,528 C100,500 210,520 280,590 L0,590 Z" fill="var(--purple)"/>
    <g role="img" aria-label="Photo of a child in a purple hat wearing gloves and digging">
      <circle cx="130" cy="466" r="78" fill="url(#dig)" stroke="var(--green)" stroke-width="5"/>
    </g>
  </svg>

  <div class="brand" style="left:20px;top:26px;width:240px">
    <span class="brand__dot" style="width:38px;height:38px"></span>
    <span class="brand__name" style="font-size:21px;color:var(--purple)">Tiny Sprouts</span>
    <span class="brand__tag" style="font-size:7px">Early Development &amp; Education Centre</span>
  </div>

  <div class="abs col col--left">
    <p>Our children spend their days predominantly outdoors all year round in one of two-amazing large Naturescape playgrounds full of native trees, a running creek bed, large stepping logs, a herb, vegetable and bush tucker garden along with a recycled mud kitchen made by the children, worm farm, compost bin and chickens and a fire pit where the older children can cook over an open fire.</p>
    <p>The children are taught real life skills and do their own individual risk assessments before engaging in learning experience such as crossing a flowing river creek bed, walking along logs, and climbing &amp; jumping off trees. They also learn whittling, lighting fires (using steel flints), use proper hand tools such as hacksaws, hammers and manual hand drills and learn how to navigate uneven terrains.</p>
    <p>The significant importance of learning through play while outdoors in a natural environment cannot be underestimated.</p>
  </div>

  <blockquote class="abs quote">
    “Passion is lifted from the earth itself by the muddy hands of the young; it travels along grass stained sleeves to the heart. If we are going to save environmentalism and the environment we must also save an endangered indicator species: <strong>the child in nature.</strong>”
    <cite>R. Linden</cite>
  </blockquote>

  <div class="abs col col--mid">
    <p>Just as importantly the children are able to explore and play at their own pace and set their own rhythm.</p>
    <p>In relation to children’s wellbeing, long-term outdoor preschool programmes were found to have positive impacts on both children’s physical and mental health. The studies found that as well as promoting wellbeing in children, the programmes enhance their confidence and resilience, persistence and problem-solving skills.</p>
    <p>Children’s confidence increased, and they had heightened levels of self-belief, positive attitude, independence and demonstrated an increased ability to take initiatives.</p>
    <p>Children who play regularly in natural settings are sick less often. Mud, sand, water, leaves, sticks, pine cones and gum nuts can help to stimulate children’s immune system as well as their imagination.</p>
    <p>Children who spend more time outside tend to be more physically active and are less likely to be overweight. They are more resistant to stress; have lower incidence of behavioural disorders, anxiety and depression; and have a higher measure of self-worth.</p>
    <p>Children who play in natural settings play in more diverse, imaginative and creative ways and show improved language and collaboration skills They also have more positive feelings about each other.</p>
  </div>

  <div class="abs col col--right">
    <p>Since 2015, throughout each school term our educators run free lessons for all ages in the following: meditation, yoga, sign language, Spanish, German, Malaysian, Sri Lankan Culture, Sustainability, Noongar Culture &amp; Sport.</p>
    <p>The sign language is a particular hit with the mothers as the babies are able to sign to their parents when they are hungry or need to go to the toilet before they even start talking.</p>
    <p>The first five years of a child’s development are the most crucial with 90% of their brain synapsis being formed by this time.</p>
    <p>Becoming multilingual or being able to sign has an expediential effect on the children’s development outcomes which is why we offer such a vast array of authentic leaning experiences.</p>
    <p>We believe that the best developmental outcomes occur when children who wander, wonder and play are also learning. It happens when children’s interests and passions are respected and nurtured and when educators shift their agenda away from imparting knowledge that we consider worthy, to showing children that we value their curiosity, problem solving, questions, and theories.</p>
  </div>

  <p class="abs closing">“Early childhood is the most important time for brain development. It is the time in a child’s life where they start building their brain connections and therefore, ultimately, the work we do will shape their life forever”.</p>
  <div class="abs webcorner">www.tinysprouts.example</div>
</section>

</body>
</html>
```